drink bottle label

Our drink is called VELMORA zi, a 2000 year old Asian formula for a fermented green tea drink. Flavored with organic ginger juice, cinnamon and lime. Very tasty and refreshing, good for sports recovery, digestion,liver detox,overall health and vitality. Naturally fermented creating a- no sugar, low GI, salt,-fat and gluten free- fizzy drink alternative to soft drink, sports drinks or beer. The bottle is a brown 330ml long neck bottle. For the diet and health conscious individual. We would like the label to be upmarket for restaurants & trendy organic food suppliers.
Updates

Reason: Take more time to get the best result

The bottle is brown. Try using black-gold-silver-white for the subject in a white or silver border

Target Market(s)

Upmarket, for restaurant & trendy organic food supplies.Sophisticated Health conscious people who don't want high sugar, caffeine drinks.

Industry/Entity Type

Health

Requirements
Must have
• The drink name and registered brand is" VELMORA zi."
Must feature PROBIOTICS & ENZYMES for detox.No artificial preservatives or colours. 100% Organic & raw living culture.Low GI low calorie- no cane sugar, no salt-
- no lactose, Coeliac -diabetic & vegan friendly. Ginger Brew.
Nice to have
• tastes great-revitalize- 330ml brown bottle

```html
<!DOCTYPE html>
<html lang="en">
<head>
<meta charset="utf-8">
<title>VELMORA zi. – Ginger Brew label</title>
<link rel="stylesheet" href="https://fonts.googleapis.com/css2?family=Patrick+Hand&display=swap">
<style>
  :root {
    --lime: #dfea5b;
    --navy: #1e2747;
    --cream: #fbfbe1;
    --hand: "Patrick Hand", cursive;
  }
  * { margin: 0; padding: 0; box-sizing: border-box; }
  html, body { width: 982px; height: 1200px; overflow: hidden; background: var(--lime); }
  .label {
    position: relative;
    width: 982px; height: 1200px;
    background: var(--lime);
    font-family: var(--hand);
    color: var(--navy);
  }
  .label > * { position: absolute; }

  .tagline {
    left: 62px; top: 40px;
    font-size: 68px; line-height: 0.95;
    transform: rotate(-14deg);
    text-align: center;
    letter-spacing: 2px;
  }
  .tagline-arrow { left: 365px; top: 82px; width: 100px; height: 110px; }

  .brand-name {
    left: 43px; top: 245px; width: 900px; height: 197px;
    display: flex; align-items: center; justify-content: center;
    color: var(--navy);
    font-size: 150px; font-weight: 400; letter-spacing: 6px; line-height: 1;
    white-space: nowrap;
  }

  .claims-left { left: 40px; top: 510px; width: 330px; text-align: center; font-size: 44px; line-height: 1.35; }
  .claims-left .plain { display: block; }
  .pill {
    background: var(--navy); color: var(--cream);
    border-radius: 30px; padding: 0 18px; line-height: 58px; margin-top: 3px;
  }
  .claims-left .pill { display: table; margin-left: auto; margin-right: auto; }

  .free-from {
    left: 340px; top: 545px; width: 320px;
    text-align: center; color: var(--cream);
    font-size: 44px; line-height: 1.2;
  }

  .revitalize {
    left: 678px; top: 590px; width: 236px; height: 90px;
    background: var(--cream); border-radius: 48% 52% 45% 55% / 55% 48% 52% 45%;
    display: flex; align-items: center; justify-content: center;
    font-size: 48px;
  }

  .probiotics { left: 440px; top: 728px; width: 500px; text-align: center; line-height: 1.1; }
  .probiotics .headline { font-size: 40px; text-decoration: underline; text-underline-offset: 6px; text-decoration-thickness: 3px; }
  .probiotics .sub { font-size: 38px; }

  .flavour {
    left: 153px; top: 859px; width: 146px; height: 146px;
    border: 4px solid var(--cream); border-radius: 50%;
    color: var(--cream); font-size: 46px; line-height: 1.05;
    display: flex; align-items: center; justify-content: center; text-align: center;
  }

  .volume {
    left: 69px; top: 1058px; width: 127px; height: 60px;
    background: var(--cream); border-radius: 50% 45% 52% 48% / 55% 50% 50% 45%;
    display: flex; align-items: center; justify-content: center; font-size: 40px;
  }

  .diet-friendly { left: 330px; top: 815px; width: 224px; text-align: center; font-size: 48px; line-height: 1.15; }
  .amp {
    display: flex; align-items: center; justify-content: center;
    width: 60px; height: 60px; margin: 6px auto;
    background: var(--navy); color: var(--cream); border-radius: 50%; font-size: 44px;
  }

  .organic-badge {
    left: 566px; top: 880px; width: 370px; height: 248px;
    background: var(--navy); color: var(--cream);
    border-radius: 46% 54% 50% 50% / 52% 48% 52% 48%;
    display: flex; align-items: center; justify-content: center; text-align: center;
    font-size: 46px; line-height: 1.2; letter-spacing: 1px;
  }
</style>
</head>
<body>
<main class="label">
  <p class="tagline">tastes<br>great!</p>
  <svg class="tagline-arrow" viewBox="0 0 100 110" aria-hidden="true">
    <path d="M70 104 C88 66 72 28 28 22" fill="none" stroke="#1e2747" stroke-width="5" stroke-linecap="round"/>
    <path d="M44 8 L24 22 L42 38" fill="none" stroke="#1e2747" stroke-width="5" stroke-linecap="round" stroke-linejoin="round"/>
  </svg>

  <h1 class="brand-name">VELMORA zi.</h1>

  <div class="claims-left">
    <span class="plain">Low GI</span>
    <span class="plain">low calorie</span>
    <span class="pill">no cane sugar</span>
    <span class="pill">no salt</span>
    <span class="pill">no lactose</span>
  </div>

  <p class="free-from">No artificial<br>preservatives<br>or colours</p>

  <p class="revitalize">revitalize</p>

  <div class="probiotics">
    <p class="headline">PROBIOTICS &amp; ENZYMES</p>
    <p class="sub">for detox</p>
  </div>

  <p class="flavour">Ginger<br>Brew</p>

  <p class="volume">330ml</p>

  <div class="diet-friendly">
    <p>Coeliac,<br>diabetic</p>
    <span class="amp">&amp;</span>
    <p>vegan<br>friendly</p>
  </div>

  <p class="organic-badge">100%<br>ORGANIC &amp; RAW<br>LIVING CULTURE</p>
</main>
</body>
</html>
```